Business Card Design

Online clothing womens clothing store, I sell my clothing online and at the markets.

i would like the attached picture on the front of the card and the contact information on the back.

Industry/Entity Type

Business

Contact Information for Business Card

Velvet Harbour
Marnie Talbot
(Instagram symbol) _velvet_harbour_
(Facebook symbol) www.facepage-example.com/velvetharbourau/

W : www.velvetharbour-example.com.au
E : info@velvetharbour-example.com.au
P : 0491876324

```html
<!DOCTYPE html>
<html lang="en">
<head>
<meta charset="utf-8">
<title>Velvet Harbour – Business Card</title>
<link href="https://fonts.googleapis.com/css2?family=Barlow:wght@400&family=Barlow+Condensed:wght@600&family=Source+Sans+3:wght@400;600&display=swap" rel="stylesheet">
<style>
  :root {
    --page: #efefef;
    --paper: #ffffff;
    --ink: #111111;
    --band: #000000;
    --reverse: #ffffff;
    --photo-light: #dfe5e8;
    --photo-mid: #9fb1b5;
    --photo-dark: #4a4f50;
    --rule: #d0d0d0;
  }
  * { margin: 0; padding: 0; box-sizing: border-box; }
  html, body {
    width: 1189px; height: 1200px; overflow: hidden;
    background: var(--page);
  }
  .card {
    position: absolute; left: 206px; width: 777px; height: 478px;
    background: var(--paper); overflow: hidden;
  }
  .card--front { top: 87px; }
  .card--back { top: 635px; }

  /* Front */
  .front-photo {
    position: absolute; left: 0; top: 0; width: 600px; height: 100%;
    background:
      radial-gradient(ellipse 55% 70% at 82% 35%, var(--photo-dark) 0%, rgba(74,79,80,0.6) 45%, rgba(74,79,80,0) 80%),
      linear-gradient(100deg, var(--photo-light) 0%, #c9d4d7 40%, var(--photo-mid) 70%, #6f7a7b 100%);
  }
  .front-photo__title {
    position: absolute; left: 32px; bottom: 28px; width: 546px; height: 84px;
    overflow: visible;
  }
  .front-photo__title text {
    font-family: "Barlow Condensed", sans-serif; font-weight: 600;
    font-size: 84px; fill: var(--reverse);
  }
  .front-strip {
    position: absolute; left: 600px; top: 0; width: 177px; height: 100%;
    border-left: 1px solid var(--rule);
  }
  .front-strip__name {
    position: absolute; left: 50%; top: 50%;
    transform: translate(-50%, -50%) rotate(-90deg);
    font-family: "Barlow", sans-serif; font-weight: 400;
    font-size: 37px; letter-spacing: 0.2em; color: var(--ink);
    white-space: nowrap;
  }

  /* Back */
  .back-brand {
    position: absolute; left: 0; top: 0; width: 100%; height: 248px;
    display: flex; align-items: center; justify-content: center;
  }
  .back-brand__name {
    font-family: "Barlow", sans-serif; font-weight: 400;
    font-size: 62px; letter-spacing: 0.16em; color: var(--ink);
    white-space: nowrap; margin-top: -12px;
  }
  .back-band {
    position: absolute; left: 0; top: 248px; width: 100%; height: 230px;
    background: var(--band); color: var(--reverse);
    font-family: "Source Sans 3", sans-serif;
  }
  .person {
    position: absolute; right: 432px; top: 80px; text-align: right;
  }
  .person__name { font-size: 29px; font-weight: 600; line-height: 1.05; }
  .person__role { font-size: 19px; font-weight: 400; line-height: 1.2; }
  .divider {
    position: absolute; left: 389px; top: 66px; width: 2px; height: 100px;
    background: var(--reverse);
  }
  .contacts {
    position: absolute; left: 430px; top: 66px; list-style: none;
  }
  .contacts li {
    display: flex; align-items: center; height: 25px;
    font-size: 19px; line-height: 1; white-space: nowrap;
  }
  .contacts .icon {
    width: 20px; height: 20px; margin-right: 8px; flex: none;
  }
  .icon--plain {
    border: 2px solid var(--reverse); border-radius: 4px;
  }
</style>
</head>
<body>
  <section class="card card--front">
    <div class="front-photo" role="img" aria-label="Misty photograph of a woman with long tousled hair seen from the side, wrapped in pale blue smoke">
      <svg class="front-photo__title" viewBox="0 0 546 84" aria-label="VELVET HARBOUR">
        <text x="0" y="78" textLength="546" lengthAdjust="spacingAndGlyphs">VELVET HARBOUR</text>
      </svg>
    </div>
    <div class="front-strip">
      <div class="front-strip__name">VELVET HARBOUR</div>
    </div>
  </section>

  <section class="card card--back">
    <div class="back-brand">
      <div class="back-brand__name">VELVET HARBOUR</div>
    </div>
    <div class="back-band">
      <div class="person">
        <div class="person__name">Marnie Talbot</div>
        <div class="person__role">Managing Director</div>
      </div>
      <div class="divider"></div>
      <ul class="contacts">
        <li>
          <svg class="icon" viewBox="0 0 20 20" aria-hidden="true">
            <rect width="20" height="20" rx="3" fill="#fff"/>
            <path d="M4 8c0-2 3-3 6-3s6 1 6 3v1h-3V7.5H7V9H4z" fill="#000"/>
            <rect x="6" y="10" width="8" height="6" rx="1" fill="#000"/>
          </svg>
          0491876324
        </li>
        <li>
          <svg class="icon" viewBox="0 0 20 20" aria-hidden="true">
            <rect width="20" height="20" rx="3" fill="#fff"/>
            <rect x="3.5" y="5.5" width="13" height="9" fill="none" stroke="#000" stroke-width="1.4"/>
            <path d="M3.5 5.5l6.5 5 6.5-5M3.5 14.5l5-4.5M16.5 14.5l-5-4.5" fill="none" stroke="#000" stroke-width="1.2"/>
          </svg>
          info@velvetharbour-example.com.au
        </li>
        <li><span class="icon icon--plain"></span>_velvet_harbour_</li>
        <li><span class="icon icon--plain"></span>velvetharbourau</li>
      </ul>
    </div>
  </section>
</body>
</html>
```